Elegant, exclusive brand Folder design for International division

Our International desk division requires a new folder design for its very exclusive clients. So far we have a design but is not reaching our expectations. We want something very clean, classy and elegant. A folder that represents our brand the best way possible.

Marlow Tressby is Australia’s leading buyer’s Agency. We help buyers get their dream home at the best price, time and location. For our International clients we offer a much more exclusive service, we want to differentiate this two clients through our stationary.

-We are currently developing an International Division website, but for now here is the link of our website: http://www.marlowtressby.com.au/

Once the design is done we would need recommendations on paper, printing and cutting patterns (in case it applies) to make this folder look stunning.

Files attached:
-Folder ideas
-Marlow Tressby brand guidelines
-Marlow Tressby logo and monogram
-Current Folder

Target Market(s)

International clients -Property investment clients with really high budgets looking for high-quality, beautiful and exclusive primary residence or investment properties in Australia.

Most of our clients are located in Europe and Asia.

Industry/Entity Type

Real Estate

Font styles to use
Sans Serif

Colors
33b8a4
1b1b1b
333333
ffffff

Requirements
Must have
• Should be creative but very clean, luxuriously and exclusive.
• We require a full recommendation and guidance on:
• -Type of paper
• -Cutting patterns
• -Printing colours and styles
• Our colours are dark grey -we are ok with silver also :
• R83 / G86 / B90
• OR
• R40 / G44 / B42
• Aquamarine:
• R0 / G178 / B169
• We are not fans of the aquamarine colour for background uses

```html
<!DOCTYPE html>
<html lang="en">
<head>
<meta charset="utf-8">
<title>Marlow Tressby – International Folder</title>
<link rel="stylesheet" href="https://fonts.googleapis.com/css2?family=Tenor+Sans&display=swap">
<style>
  :root {
    --backdrop: #e4e4e4;
    --folder-dark: #181c24;
    --flap-dark: #1b1f27;
    --aqua: #22a896;
    --aqua-deep: #1a8f7f;
    --aqua-light: #35bca8;
    --ink: #16262a;
    --paper: #ffffff;
    --dieline: #c8157c;
    --crop: #9a9a9a;
    --shadow: #0c0e12;
  }
  html, body {
    margin: 0;
    padding: 0;
    width: 800px;
    height: 1200px;
    overflow: hidden;
    background: var(--backdrop);
  }
  .canvas {
    width: 800px;
    height: 1200px;
    display: flex;
    align-items: center;
    justify-content: center;
  }
  .folder-flat {
    width: 770px;
    height: 570px;
    display: block;
  }
  .panel-dark { fill: var(--folder-dark); }
  .flap-dark { fill: var(--flap-dark); }
  .flap-aqua { fill: var(--aqua-deep); }
  .beam { fill: url(#beamTone); }
  .emblem-shadow { fill: var(--shadow); }
  .emblem-disc { fill: var(--aqua); }
  .cut-line, .fold-line {
    fill: none;
    stroke: var(--dieline);
    stroke-width: 1;
  }
  .fold-line { stroke-dasharray: 2 3; }
  .crop-mark { stroke: var(--crop); stroke-width: 1; }
  .brand-name {
    font-family: "Tenor Sans", sans-serif;
    font-size: 27px;
    letter-spacing: 3px;
    fill: var(--ink);
  }
  .brand-url {
    font-family: "Tenor Sans", sans-serif;
    font-size: 13px;
    letter-spacing: 0.3px;
    fill: var(--paper);
  }
  .emblem-name {
    font-family: "Tenor Sans", sans-serif;
    font-size: 19px;
    letter-spacing: 2px;
    fill: var(--paper);
    text-anchor: middle;
  }
</style>
</head>
<body>
<main class="canvas">
  <svg class="folder-flat" viewBox="60 760 865 640" xmlns="http://www.w3.org/2000/svg" aria-label="Marlow Tressby presentation folder, flat die layout">
    <defs>
      <linearGradient id="beamTone" x1="0" y1="0" x2="1" y2="1">
        <stop offset="0" stop-color="#1f9c8a"/>
        <stop offset="0.5" stop-color="#27b09c"/>
        <stop offset="1" stop-color="#1c9583"/>
      </linearGradient>
    </defs>

    <!-- crop marks -->
    <g class="crop-marks">
      <line class="crop-mark" x1="94" y1="764" x2="94" y2="780"/>
      <line class="crop-mark" x1="66" y1="791" x2="84" y2="791"/>
      <line class="crop-mark" x1="892" y1="764" x2="892" y2="780"/>
      <line class="crop-mark" x1="902" y1="791" x2="920" y2="791"/>
      <line class="crop-mark" x1="94" y1="1374" x2="94" y2="1392"/>
      <line class="crop-mark" x1="66" y1="1364" x2="84" y2="1364"/>
      <line class="crop-mark" x1="892" y1="1374" x2="892" y2="1392"/>
      <line class="crop-mark" x1="902" y1="1364" x2="920" y2="1364"/>
    </g>

    <!-- folder body -->
    <g class="folder-body">
      <rect class="flap-aqua" x="83" y="878" width="92" height="377"/>
      <rect class="flap-dark" x="820" y="878" width="82" height="377"/>
      <rect class="panel-dark" x="172" y="782" width="651" height="472"/>
      <rect class="panel-dark" x="162" y="1250" width="661" height="128"/>
    </g>

    <!-- aqua light beam -->
    <polygon class="beam" role="img" aria-label="Faceted aquamarine geometric pattern in a beam shape"
             points="155,782 172,782 585,942 578,1068 172,1250 155,1250"/>

    <!-- emblem -->
    <g class="emblem">
      <circle class="emblem-shadow" cx="628" cy="1010" r="76"/>
      <circle class="emblem-disc" cx="638" cy="1005" r="76"/>
      <text class="emblem-name" x="638" y="1000">MARLOW</text>
      <text class="emblem-name" x="638" y="1025">TRESSBY</text>
    </g>

    <!-- spine text -->
    <g class="spine-text">
      <text class="brand-name" transform="translate(219 1202) rotate(-90)">MARLOW TRESSBY</text>
      <text class="brand-url" transform="translate(239 1196) rotate(-90)">www.marlowtressby.com.au</text>
    </g>

    <!-- dieline -->
    <g class="dieline">
      <polyline class="fold-line" points="172,792 812,792"/>
      <polyline class="fold-line" points="172,792 172,1250"/>
      <polyline class="fold-line" points="812,792 812,1250"/>
      <polyline class="fold-line" points="172,1250 812,1250"/>

      <path class="cut-line" d="M172 885 L95 940 L95 1220 L172 1250"/>
      <path class="cut-line" d="M812 885 L890 940 L890 1220 L812 1250"/>
      <path class="cut-line" d="M130 1132 L130 1170 L140 1190"/>
      <path class="cut-line" d="M856 1132 L856 1170 L846 1190"/>

      <path class="cut-line" d="M175 1250 L206 1310 L190 1312 Q176 1318 177 1340 L178 1352 Q180 1364 195 1365 L462 1365 L492 1250"/>
      <path class="cut-line" d="M497 1250 L518 1365 L790 1365 Q806 1364 808 1350 L808 1335 Q806 1314 780 1310 L812 1250"/>
      <line class="cut-line" x1="430" y1="1270" x2="452" y2="1288"/>
      <line class="cut-line" x1="318" y1="1332" x2="340" y2="1350"/>
      <line class="cut-line" x1="555" y1="1270" x2="533" y2="1288"/>
      <line class="cut-line" x1="668" y1="1332" x2="646" y2="1350"/>
    </g>
  </svg>
</main>
</body>
</html>
```